qv motor spares (www.qv-motorspares.example) needs a logo box design

we need to design 2 new box for same brand with colour and same design for our company which is specialist with auto parts to be produced in china, brake pads of same brand (Taliren) the colour is Light blue or Azure and olive colour for lines the only difference between the boxes is the type which is brake pads or brake shoes only

below the logo it should be written Calveron, Marelia
(not made in)

all details are in the attached file

once you finish please send it as 2d and 3d pdf file

Target Market(s)

AUTO PARTS PARTS

Font styles to use
Script

Colors
33a6d7
add136

Requirements
Must have
• formula
logo
brand name
email: info@qv-motorspares.example
Nice to have
• LOGO ON THE BOX THAT STANDS FOR THE NAME OF THE BRAND
THE BRAND NAME
THE CITY OF PRODUCTION AND COUNTRY BUT WITHOUT WRITING MADE IN
THE FORMULA
SOME SAFETY RULES
ATTRACTIVE COLOURS AND DESIGNS
SOME LABELS AND ATTRACTIVE FEATURES
TAKE AS REFERENSE MORVAL BRAKE PADS BRAND

```html
<!DOCTYPE html>
<html lang="en">
<head>
<meta charset="utf-8">
<title>Taliren Brake Pads – Box Dieline</title>
<link href="https://fonts.googleapis.com/css2?family=Montserrat:wght@500;600;700&family=Questrial&family=Exo+2:ital,wght@1,800&display=swap" rel="stylesheet">
<style>
  :root{
    --navy:#1f2461;
    --sky:#37aae2;
    --sky-light:#5fc6f4;
    --red:#e4232b;
    --cut:#e8323c;
    --white:#ffffff;
    --pad-dark:#4a4c50;
    --pad-light:#8a8c90;
  }
  html,body{margin:0;padding:0;overflow:hidden;background:var(--white);}
  .canvas{width:1200px;height:1200px;display:block;}
  .cut-line{fill:none;stroke:var(--cut);stroke-width:1.2;}
  .panel-navy{fill:var(--navy);}
  .brand-name{font-family:"Montserrat",sans-serif;font-weight:700;fill:var(--white);}
  .brand-sub{font-family:"Montserrat",sans-serif;font-weight:700;fill:var(--white);}
  .body-copy{font-family:"Questrial",sans-serif;fill:var(--white);}
  .body-strong{font-family:"Montserrat",sans-serif;font-weight:600;fill:var(--white);}
  .web{font-family:"Montserrat",sans-serif;font-weight:600;fill:var(--white);}
  .headline{font-family:"Montserrat",sans-serif;font-weight:700;fill:var(--white);stroke:#1b5f8f;stroke-width:1.2;paint-order:stroke;}
  .label-italic{font-family:"Exo 2",sans-serif;font-style:italic;font-weight:800;fill:var(--white);}
  .bullet{fill:var(--red);}
  .rule{stroke:var(--white);stroke-width:1;}
</style>
</head>
<body>
<svg class="canvas" viewBox="0 0 1500 1500" xmlns="http://www.w3.org/2000/svg">
  <defs>
    <linearGradient id="skyGrad" x1="0" y1="0" x2="1" y2="1">
      <stop offset="0" stop-color="var(--sky)"/>
      <stop offset="1" stop-color="var(--sky-light)"/>
    </linearGradient>
    <linearGradient id="padGrad" x1="0" y1="0" x2="1" y2="1">
      <stop offset="0" stop-color="var(--pad-light)"/>
      <stop offset="1" stop-color="var(--pad-dark)"/>
    </linearGradient>
  </defs>

  <g class="dieline">
    <path class="cut-line" d="M412 95 L265 95 L220 110 L220 225 L245 238 L412 245"/>
    <path class="cut-line" d="M1086 95 L1235 95 L1280 110 L1280 225 L1255 238 L1086 245"/>
    <path class="cut-line" d="M235 265 L115 265 L70 280 L70 395 L58 410 L58 555 L70 570 L70 680 L200 682 L200 695 L235 695"/>
    <path class="cut-line" d="M1263 260 L1298 260 L1298 273 L1428 273 L1428 395 L1440 410 L1440 555 L1428 570 L1428 680 L1385 695 L1263 695"/>
    <path class="cut-line" d="M412 713 L250 720 L218 730 L218 845 L250 862 L412 862"/>
    <path class="cut-line" d="M1086 713 L1248 720 L1280 730 L1280 845 L1248 862 L1086 862"/>
    <path class="cut-line" d="M425 870 L310 895 L262 915 L262 1255 L385 1295 L412 1303"/>
    <path class="cut-line" d="M1075 870 L1190 895 L1236 915 L1236 1255 L1113 1295 L1086 1303"/>
    <path class="cut-line" d="M412 1303 L428 1320 L428 1462 L1062 1462 L1062 1320 L1075 1303"/>
  </g>

  <g class="lid-panel">
    <rect class="panel-navy" x="412" y="37" width="674" height="222"/>
    <polygon points="412,37 668,37 598,259 412,259" fill="url(#skyGrad)"/>
    <rect x="432" y="120" width="245" height="110" rx="30" fill="url(#padGrad)" role="img" aria-label="Photo of a pair of disc brake pads"/>
    <path class="cut-line" d="M682 148 L682 70 L700 45 L800 45 L817 70 L817 148 L682 148 M682 95 L817 95 M817 120 L840 95 L1086 95"/>
    <text class="brand-name" x="937" y="178" font-size="40" text-anchor="middle">Taliren</text>
    <text class="brand-sub" x="937" y="208" font-size="18" text-anchor="middle">Brake Pads</text>
  </g>

  <g class="side-left">
    <rect x="235" y="259" width="177" height="436" fill="url(#skyGrad)"/>
    <g transform="translate(300 477) rotate(-90)">
      <text class="brand-name" x="0" y="0" font-size="40" text-anchor="middle">Taliren</text>
      <text class="brand-sub" x="0" y="36" font-size="19" text-anchor="middle">Brake Pads</text>
    </g>
    <text class="web" transform="translate(391 477) rotate(-90)" font-size="13" text-anchor="middle">WWW.QV-MOTORSPARES.EXAMPLE</text>
  </g>

  <g class="main-face">
    <rect class="panel-navy" x="412" y="259" width="674" height="436"/>
    <text class="brand-name" x="465" y="358" font-size="66">Taliren</text>
    <text class="brand-sub" x="465" y="398" font-size="25">Brake Pads</text>
    <text class="body-strong" x="465" y="440" font-size="12">Disc Brake Pads</text>
    <text class="body-copy" x="465" y="472" font-size="13">100% Asbestos Free</text>
    <text class="body-copy" x="465" y="504" font-size="13">Limited Warranty</text>
    <text class="body-copy" x="465" y="521" font-size="13">(See Retailer for Details)</text>
    <g font-size="12">
      <polygon class="bullet" points="456,540 461,544.5 456,549"/>
      <text class="body-copy" x="465" y="549">Reduced noise with shims where applicable</text>
      <polygon class="bullet" points="456,561 461,565.5 456,570"/>
      <text class="body-copy" x="465" y="570">Extended wear life and quieter operation high tech-</text>
      <text class="body-copy" x="465" y="584">nology manufacturing</text>
      <polygon class="bullet" points="456,596 461,600.5 456,605"/>
      <text class="body-copy" x="465" y="605">Consistent braking performance throughout the life</text>
      <text class="body-copy" x="465" y="619">of the pads</text>
    </g>
    <text class="brand-name" x="955" y="596" font-size="30" text-anchor="middle">Taliren</text>
    <text class="brand-sub" x="955" y="614" font-size="12" text-anchor="middle">Brake Pads</text>
    <text class="body-copy" x="955" y="636" font-size="13" text-anchor="middle">Taliren</text>
    <text class="body-copy" x="955" y="652" font-size="13" text-anchor="middle">info@qv-motorspares.example</text>
    <text class="body-copy" x="955" y="668" font-size="13" text-anchor="middle">Calveron, Marelia</text>
  </g>

  <g class="side-right">
    <rect class="panel-navy" x="1086" y="259" width="177" height="436"/>
    <g transform="translate(1198 477) rotate(90)">
      <text class="brand-name" x="0" y="0" font-size="40" text-anchor="middle">Taliren</text>
      <text class="brand-sub" x="0" y="36" font-size="19" text-anchor="middle">Brake Pads</text>
    </g>
    <text class="web" transform="translate(1108 477) rotate(90)" font-size="13" text-anchor="middle">WWW.QV-MOTORSPARES.EXAMPLE</text>
  </g>

  <g class="front-band">
    <rect class="panel-navy" x="412" y="695" width="674" height="172"/>
    <g transform="translate(598 790) rotate(180)">
      <text class="brand-name" x="0" y="0" font-size="44" text-anchor="middle">Taliren</text>
      <text class="brand-sub" x="0" y="32" font-size="18" text-anchor="middle">Brake Pads</text>
    </g>
    <rect x="812" y="714" width="248" height="124" rx="30" fill="url(#padGrad)" role="img" aria-label="Photo of a pair of disc brake pads"/>
  </g>

  <g class="display-face">
    <rect class="panel-navy" x="412" y="867" width="674" height="436"/>
    <polygon points="412,867 806,867 652,1303 412,1303" fill="url(#skyGrad)"/>
    <text class="headline" x="450" y="956" font-size="47">Professional</text>
    <text class="body-strong" x="450" y="1037" font-size="27">Disk brake pads</text>
    <text class="body-copy" x="450" y="1058" font-size="17">100% Asbestos free</text>
    <line class="rule" x1="450" y1="1064" x2="684" y2="1064"/>
    <text class="body-strong" x="450" y="1093" font-size="16">Plaquettes de freins a' disque</text>
    <text class="body-copy" x="450" y="1114" font-size="17">100% sans amiante</text>
    <line class="rule" x1="450" y1="1120" x2="684" y2="1120"/>
    <polygon points="412,1181 690,1181 676,1220 412,1220" fill="var(--red)"/>
    <text class="label-italic" x="562" y="1208" font-size="21" text-anchor="middle">SEMI-METALIC</text>
    <text class="brand-name" x="937" y="938" font-size="48" text-anchor="middle">Taliren</text>
    <text class="brand-sub" x="937" y="968" font-size="20" text-anchor="middle">Brake Pads</text>
    <path d="M760 1030 L1000 1040 L1055 1075 L1086 1100 L1086 1303 L1040 1303 L980 1275 L740 1240 L705 1180 Z" fill="url(#padGrad)" role="img" aria-label="Close-up photo of a disc brake pad set"/>
  </g>
</svg>
</body>
</html>
```